Professional/modern business card design for construction company

We need a new business card design, double sided keeping it modern, sleek, professional and simple. We are an earthmoving business but do not want any pictures of machinery. I would like one side to have the logo and the other to have all the information, keeping with the colors in our logo. The business card will need to be able to be customised so we can use it for several different managers., we would also like to be able to use the design to apply it to other stationary ie. letterheads, notebooks etc. We do not really have a tag line but we could put on there that we specialise in - Agriculture, Civil Construction and Mining.

Contact Information for Business Card

Brolga Ridge Excavations Pty Ltd
ABN 58 402 937 615
82 Gumleaf Creek Road, Moree NSW 2400

Harold Benton
Managing Director
P 0418 639 204
E haroldbenton@brolgaridgeexc.com.au

Font styles to use
Serif
Sans Serif

Requirements
Nice to have
• I have attached some examples of ideas.
Should not have
• images of machinery

```html
<!DOCTYPE html>
<html lang="en">
<head>
<meta charset="utf-8">
<title>Brolga Ridge Excavations – Business Card</title>
<link href="https://fonts.googleapis.com/css2?family=Poppins:wght@400;500;600;700&display=swap" rel="stylesheet">
<style>
  :root {
    --charcoal: #3b3b3c;
    --charcoal-deep: #333334;
    --orange: #ec7f1c;
    --paper: #f7f7f7;
    --ink: #2e2e2e;
    --rule: #8a8a8a;
    --backdrop: #d9d9d9;
  }
  * { margin: 0; padding: 0; box-sizing: border-box; }
  html, body {
    width: 1200px; height: 1021px; overflow: hidden;
    background: var(--backdrop);
    font-family: "Poppins", Arial, sans-serif;
  }
  .canvas {
    width: 1200px; height: 1021px;
    display: flex; flex-direction: column; align-items: center; justify-content: center;
    gap: 44px;
  }
  .card {
    position: relative;
    width: 760px; height: 434px;
    overflow: hidden;
    box-shadow: 0 6px 18px rgba(0,0,0,0.18);
  }
  .card-shapes { position: absolute; inset: 0; }

  /* Front */
  .card--front { background: var(--charcoal); }
  .front-name {
    position: absolute; left: 0; right: 0; top: 130px;
    text-align: center; color: #f0f0f0;
    font-weight: 700; font-size: 40px; line-height: 1.12; letter-spacing: 0.5px;
  }
  .front-name .legal { display: block; font-size: 40px; }
  .tagline {
    position: absolute; left: 160px; top: 336px;
    color: #f2f2f2; font-size: 17px; letter-spacing: 1.2px; font-weight: 400;
    text-transform: uppercase;
  }
  .tagline .divider { color: var(--orange); margin: 0 10px; }

  /* Back */
  .card--back { background: var(--paper); }
  .back-name {
    position: absolute; left: 44px; top: 100px; width: 300px;
    color: var(--charcoal); font-weight: 700; font-size: 29px; line-height: 1.15;
  }
  .column-rule {
    position: absolute; left: 376px; top: 60px; width: 1.5px; height: 210px;
    background: var(--rule);
  }
  .contact {
    position: absolute; left: 398px; top: 62px;
    color: var(--ink); font-size: 17px; line-height: 1.45;
  }
  .contact-name { color: var(--orange); font-weight: 700; font-size: 25px; line-height: 1.1; }
  .contact-title { font-size: 17px; margin-bottom: 12px; }
  .contact-address { margin-bottom: 4px; }
  .contact-line { display: flex; align-items: center; gap: 8px; }
  .contact-line svg { width: 15px; height: 15px; flex: none; }
  .abn {
    position: absolute; left: 270px; width: 290px; top: 350px;
    text-align: center; color: #f0f0f0; font-size: 20px; letter-spacing: 0.5px;
  }
  .abn .label { color: var(--orange); }
</style>
</head>
<body>
<main class="canvas">

  <section class="card card--front" aria-label="Business card front">
    <svg class="card-shapes" viewBox="0 0 760 434" aria-hidden="true">
      <polygon points="120,374 716,374 742,400 120,400" fill="var(--orange)"/>
    </svg>
    <h1 class="front-name">Brolga Ridge<span class="legal">Excavations Pty Ltd</span></h1>
    <p class="tagline">Agriculture<span class="divider">|</span>Civil Construction<span class="divider">|</span>Mining</p>
  </section>

  <section class="card card--back" aria-label="Business card back">
    <svg class="card-shapes" viewBox="0 0 760 434" aria-hidden="true">
      <polygon points="0,300 262,300 254,314 0,314" fill="var(--orange)"/>
      <polygon points="0,322 250,322 270,298 560,298 580,350 760,350 760,434 0,434" fill="var(--charcoal)"/>
      <polygon points="573,330 760,330 760,344 579,344" fill="var(--orange)"/>
    </svg>

    <h2 class="back-name">Brolga Ridge Excavations Pty Ltd</h2>
    <div class="column-rule"></div>

    <div class="contact">
      <p class="contact-name">Harold Benton</p>
      <p class="contact-title">Managing Director</p>
      <p class="contact-address">82 Gumleaf Creek Road<br>Moree NSW 2400</p>
      <p class="contact-line">
        <svg viewBox="0 0 16 16"><path d="M3.5 1.5l2.5 0 1 3.5-1.8 1.2a9 9 0 0 0 4.6 4.6l1.2-1.8 3.5 1v2.5c0 .8-.7 1.5-1.5 1.5A12 12 0 0 1 2 3c0-.8.7-1.5 1.5-1.5z" fill="var(--orange)"/></svg>
        0418 639 204
      </p>
      <p class="contact-line">
        <svg viewBox="0 0 16 16"><rect x="1" y="3" width="14" height="10" fill="none" stroke="var(--orange)" stroke-width="1.6"/><path d="M1 3l7 6 7-6" fill="none" stroke="var(--orange)" stroke-width="1.6"/></svg>
        haroldbenton@brolgaridgeexc.com.au
      </p>
      <p class="contact-line">
        <svg viewBox="0 0 16 16"><circle cx="8" cy="8" r="6.5" fill="none" stroke="var(--orange)" stroke-width="1.4"/><ellipse cx="8" cy="8" rx="3" ry="6.5" fill="none" stroke="var(--orange)" stroke-width="1.2"/><path d="M1.5 8h13M2.5 4.5h11M2.5 11.5h11" stroke="var(--orange)" stroke-width="1.1"/></svg>
        www.brolgaridgeexc.com.au
      </p>
    </div>

    <p class="abn"><span class="label">ABN</span> 58 402 937 615</p>
  </section>

</main>
</body>
</html>
```